Quillfern Nightclub Flyer (Updated)

Flyer for facebook, square is fine, or rectangular. Here is the text:
QUILLFERN
Nightclub + Lounge
presents

SPLIT DECK WEDNESDAY
Nov 29 2018

CLUB FLOOR:
GORDY B2B RALPH
THEODORE BRUSKVIK

LOUNGE:
OTIS B2B HALF TIDE
COPPER FENWICK

Powered by HALVERN Acoustics
4716 Larchmere Avenue 21+ 9pm-2am
quillfernvenue-example.com for VIP booth inquiries

Target Market(s)

Nightclub

Industry/Entity Type

Night Club

Font styles to use
Sans Serif

Colors

Designer to choose colors to be used in the design.

Requirements
Must have
• All the text listed, and plz keep the theme of the attached files. We want to stay consistent with the Quillfern brand
Nice to have
• Try to stay with the theme from the attachments
Should not have
• Dont' stray to far from the general theme we have from the attachments

```html
<!DOCTYPE html>
<html lang="en">
<head>
<meta charset="utf-8">
<title>Quillfern Nightclub + Lounge — Split Deck Wednesday</title>
<link rel="stylesheet" href="https://fonts.googleapis.com/css2?family=Cinzel:wght@400;500&family=Open+Sans:wght@400&display=swap">
<style>
  :root {
    --bg: #16130f;
    --gold: #b8925a;
    --gold-light: #d9b77c;
    --white: #f4f1ea;
    --grey: #8f8c87;
  }
  html, body {
    margin: 0;
    padding: 0;
    overflow: hidden;
    background: var(--bg);
  }
  .flyer {
    position: relative;
    width: 1200px;
    height: 1200px;
    background: var(--bg);
    overflow: hidden;
    font-family: "Open Sans", Arial, sans-serif;
    color: var(--white);
  }
  .frame {
    position: absolute;
    inset: 0;
  }
  .line {
    position: absolute;
    left: 0;
    width: 100%;
    margin: 0;
    text-align: center;
    line-height: 1;
    white-space: nowrap;
  }
  .wordmark {
    top: 108px;
    font-family: "Cinzel", "Times New Roman", serif;
    font-weight: 400;
    font-size: 112px;
    letter-spacing: 2px;
    color: var(--white);
  }
  .venue-type {
    top: 255px;
    font-size: 29px;
    letter-spacing: 6px;
    color: var(--white);
  }
  .presents {
    top: 322px;
    font-size: 30px;
    color: var(--white);
  }
  .event-title {
    top: 428px;
    font-family: "Cinzel", "Times New Roman", serif;
    font-weight: 500;
    font-size: 56px;
    color: var(--gold);
  }
  .event-date {
    top: 500px;
    font-size: 42px;
    color: var(--gold);
  }
  .room {
    position: absolute;
    top: 628px;
    width: 420px;
    text-align: center;
  }
  .room--club { left: 112px; }
  .room--lounge { left: 666px; }
  .room-name {
    margin: 0;
    font-size: 31px;
    line-height: 1;
    height: 34px;
  }
  .room--club .room-name { color: var(--gold); }
  .room--lounge .room-name { color: var(--white); }
  .room-rule {
    display: block;
    width: 420px;
    height: 14px;
    margin: 12px 0 22px;
  }
  .lineup {
    margin: 0;
    padding: 0;
    list-style: none;
    font-size: 30px;
    line-height: 41px;
    color: var(--white);
  }
  .details {
    position: absolute;
    top: 866px;
    left: 0;
    width: 100%;
    margin: 0;
    text-align: center;
    font-size: 30px;
    line-height: 42px;
    color: var(--grey);
  }
  .booking {
    top: 1065px;
    font-size: 35px;
    color: var(--gold);
  }
</style>
</head>
<body>
<main class="flyer">
  <svg class="frame" width="1200" height="1200" viewBox="0 0 1200 1200" aria-hidden="true">
    <defs>
      <linearGradient id="frameGold" x1="0" y1="0" x2="1" y2="1">
        <stop offset="0" stop-color="#d9b77c"/>
        <stop offset="0.5" stop-color="#8f6c3a"/>
        <stop offset="1" stop-color="#d9b77c"/>
      </linearGradient>
    </defs>
    <rect x="30" y="30" width="1140" height="1140" fill="none" stroke="url(#frameGold)" stroke-width="2"/>
    <rect x="42" y="42" width="1116" height="1116" fill="none" stroke="url(#frameGold)" stroke-width="2"/>
  </svg>

  <h1 class="line wordmark">QUILLFERN</h1>
  <p class="line venue-type">NIGHTCLUB + LOUNGE</p>
  <p class="line presents">presents</p>

  <h2 class="line event-title">SPLIT DECK WEDNESDAY</h2>
  <p class="line event-date">Nov 29, 2018</p>

  <section class="room room--club">
    <h3 class="room-name">CLUB FLOOR</h3>
    <svg class="room-rule" viewBox="0 0 420 14" aria-hidden="true">
      <line x1="12" y1="7" x2="408" y2="7" stroke="#b8925a" stroke-width="2"/>
      <circle cx="7" cy="7" r="5" fill="#b8925a"/>
      <circle cx="413" cy="7" r="5" fill="#b8925a"/>
    </svg>
    <ul class="lineup">
      <li>GORDY B2B RALPH</li>
      <li>THEODORE BRUSKVIK</li>
    </ul>
  </section>

  <section class="room room--lounge">
    <h3 class="room-name">LOUNGE</h3>
    <svg class="room-rule" viewBox="0 0 420 14" aria-hidden="true">
      <line x1="12" y1="7" x2="408" y2="7" stroke="#b8925a" stroke-width="2"/>
      <circle cx="7" cy="7" r="5" fill="#b8925a"/>
      <circle cx="413" cy="7" r="5" fill="#b8925a"/>
    </svg>
    <ul class="lineup">
      <li>OTIS B2B HALF TIDE</li>
      <li>COPPER FENWICK</li>
    </ul>
  </section>

  <p class="details">Powered by<br>HALVERN Acoustics<br>4716 Larchmere Avenue 21+ 9pm-2am</p>

  <p class="line booking">quillfernvenue-example.com for VIP booth inquiries</p>
</main>
</body>
</html>
```